Anzeigengestaltung für Unternehmensberatung für Pflegedienste
Zielgruppe
Wir sind eine Unternehmensberatung für Pflegedienste. Es soll eine Werbeanzeige erstellt werden, mit welcher schlecht laufende Pflegedienste, die gerade in einer Krise stecken angesprochen werden,
Der slogan soll einfach klingen : Pflege neu gedaxht: wirtschaftlich, nachhaltig, zukunftssicher
Anzeige in 3 Formaten
1. Format 55.3 mm x 118 mm
2. Format 1/ halbe Seite Quer 176 x 118 mm un
3. Format d 1 x A4 _Seite
Der Name der Firma Keltor GmbH info at keltor.de Tel 0381 72958143 aus Rostock Berlin und bundesweit tätig
Aufgabenstellung
Kreativ und elegant

```html
<!DOCTYPE html>
<html lang="de">
<head>
<meta charset="utf-8">
<title>Keltor – Pflege neu gedacht</title>
<link href="https://fonts.googleapis.com/css2?family=Open+Sans:wght@400;600&display=swap" rel="stylesheet">
<style>
  :root {
    --page: #eeede9;
    --band: #f3f1ec;
    --navy: #23355a;
    --ink: #2c3444;
    --photo-dark: #1d2c45;
    --photo-mid: #3c5680;
    --photo-skin: #b88f72;
    --photo-light: #9fb4cf;
  }
  * { margin: 0; padding: 0; box-sizing: border-box; }
  html, body { width: 1200px; height: 900px; overflow: hidden; }
  body {
    background: var(--page);
    font-family: "Open Sans", sans-serif;
    color: var(--ink);
    position: relative;
  }
  .ad-band {
    position: absolute;
    left: 0; top: 170px;
    width: 1200px; height: 575px;
    background: var(--band);
    overflow: hidden;
  }
  .hero-photo {
    position: absolute;
    left: 0; top: 0;
    width: 860px; height: 575px;
    background:
      radial-gradient(ellipse 230px 170px at 380px 300px, var(--photo-skin) 0%, rgba(184,143,114,0.55) 55%, rgba(184,143,114,0) 100%),
      linear-gradient(180deg, var(--photo-light) 0%, var(--photo-mid) 22%, var(--photo-dark) 60%, var(--photo-mid) 100%);
    -webkit-mask-image: linear-gradient(90deg, #000 0%, #000 62%, rgba(0,0,0,0) 100%);
    mask-image: linear-gradient(90deg, #000 0%, #000 62%, rgba(0,0,0,0) 100%);
  }
  .brand-name {
    position: absolute;
    left: 758px; top: 208px;
    font-size: 82px;
    font-weight: 600;
    letter-spacing: 4px;
    color: var(--navy);
    line-height: 1;
  }
  .headline {
    position: absolute;
    left: 646px; top: 338px;
    font-size: 48px;
    font-weight: 600;
    color: var(--navy);
    line-height: 1.2;
    white-space: nowrap;
  }
  .subline {
    position: absolute;
    left: 644px; top: 416px;
    font-size: 26px;
    font-weight: 600;
    color: var(--ink);
    line-height: 36px;
    white-space: nowrap;
  }
  .contact-line {
    position: absolute;
    left: 643px; top: 530px;
    font-size: 16px;
    color: var(--ink);
    white-space: nowrap;
  }
  .contact-line .divider { margin: 0 12px; }
</style>
</head>
<body>
  <section class="ad-band">
    <div class="hero-photo" role="img" aria-label="Nahaufnahme gefalteter Hände einer älteren Person in Jeanskleidung, überlagert von feinen leuchtenden Netzwerklinien"></div>
    <div class="brand-name">KELTOR</div>
    <h1 class="headline">Pflege neu gedacht:</h1>
    <p class="subline">wirtschaftlich, nachhaltig,<br>zukunftssicher</p>
    <p class="contact-line">info@keltor.de<span class="divider">|</span>tel 0381 72958143<span class="divider">|</span>Rostock, Berlin &amp; Nationwide</p>
  </section>
</body>
</html>
```